Design a new homepage for a construction company.

We need is a homepage design that can transform our website. The client is looking for the followings:

DESIGN DIRECTION
The use of the multiple panes (brindle surfacing) with a single image across all sections is a design detail the client pointed to as a “touch” that we’re missing. Absolutely not something to be mimicked, but an example of something to see and say “Oh, that’s clever…or cool, or something we wouldn’t have thought of ourselves”.

WEBSITE MOOD
A corporate, modern, reliable, a friendly place to work with Happy Workers.

EXAMPLES LIKED
tolvamark.com
http://www.parvick-oden.com/
https://www.brindlesurfacing.com/

WEBSITE URL
http://zulmarbuilders.com/

IMAGES
You can use stock images of landscapes, cityscapes but don’t want to use stock construction images that could later be identified as stock images and not actually the company.

Here are some photos of the company workers. Be creative with it, impress me!
https://files.quorvanshare.net/open?id=8kTzR4mQw2LpXn7VbH3sJd9YcF6aGtUe

THE WINNER
The winner of the contest may be offered, on-going works and projects.

```html
<!DOCTYPE html>
<html lang="en">
<head>
<meta charset="utf-8">
<title>Halvern Build — Homepage</title>
<link rel="stylesheet" href="https://fonts.googleapis.com/css2?family=Arimo:wght@400;700&family=Lato:wght@400;700&family=Tinos:wght@700&display=swap">
<style>
:root{
  --red:#e8141b;
  --ink:#111;
  --grey-bg:#ececec;
  --panel:#efefef;
  --muted:#777;
  --dark:#161616;
  --footer:#000;
  --white:#fff;
}
*{margin:0;padding:0;box-sizing:border-box}
html,body{width:1200px;height:5023px;overflow:hidden;background:var(--white)}
body{position:relative;font-family:"Arimo",Arial,sans-serif;color:var(--ink)}
.abs{position:absolute}

/* header */
.site-header{left:0;top:0;width:1200px;height:52px;background:rgba(255,255,255,.95);z-index:3}
.brand{left:12px;top:6px;font-size:12px;letter-spacing:.5px;text-transform:uppercase}
.menu-btn{right:0;top:0;width:57px;height:52px;background:var(--red);display:flex;align-items:center;justify-content:center}

/* hero */
.hero{left:0;top:52px;width:1200px;height:522px;background:linear-gradient(160deg,#6f9fc4 0%,#8fb4cf 35%,#b4763e 60%,#5a4a3a 100%)}
.hero-arrow{top:225px}
.hero-copy{right:45px;top:308px;text-align:right;color:var(--white)}
.hero-title{font-size:38px;font-weight:700;line-height:39px;text-shadow:0 1px 3px rgba(0,0,0,.4)}
.hero-sub{font-size:14px;margin-top:6px}
.btn-outline{display:inline-block;margin-top:11px;border:1px solid var(--white);color:var(--white);font-size:13px;font-weight:700;padding:8px 23px;text-transform:uppercase}
.hero-scroll{left:588px;top:514px}

/* intro */
.intro{left:0;top:574px;width:1200px;height:819px;background:var(--grey-bg)}
.intro h2{position:absolute;left:0;top:72px;width:1200px;text-align:center;font-size:24px;line-height:28px;font-weight:700;text-transform:uppercase}
.intro p{position:absolute;left:212px;top:146px;width:776px;text-align:center;font-size:14px;line-height:21px;color:var(--muted)}
.video{left:209px;top:245px;width:782px;height:441px;background:linear-gradient(180deg,#5b6c7d 0%,#8d98a0 45%,#6d6a5e 80%,#4d5058 100%)}
.video-bar{left:0;bottom:0;width:782px;height:44px;background:linear-gradient(transparent,rgba(0,0,0,.55))}
.btn-dark{left:480px;top:716px;width:240px;height:33px;background:var(--ink);color:var(--white);font-size:14px;font-weight:700;text-transform:uppercase;display:flex;align-items:center;justify-content:center}

/* services */
.service{top:1407px;width:365px;height:206px;background:var(--panel);text-align:center;font-family:"Lato",sans-serif;font-size:12px;font-weight:700;text-transform:uppercase}
.service svg{position:absolute;left:157px;top:60px}
.service span{position:absolute;left:0;top:125px;width:100%}

/* stats */
.stats{left:0;top:1629px;width:1200px;height:215px;background:var(--dark);display:flex}
.stat{flex:1;text-align:center;color:var(--white);font-family:"Lato",sans-serif;border-right:1px solid #2a2a2a;padding-top:74px}
.stat:last-child{border-right:0}
.stat b{display:block;font-size:34px;font-weight:400;line-height:38px}
.stat small{display:block;font-size:15px;color:#7a7a7a;margin-top:4px}

/* feature rows */
.feature{left:0;width:1200px;height:467px}
.feature .photo{position:absolute;top:0;height:467px;width:700px}
.feature .copy{position:absolute;top:0;height:467px;width:500px;display:flex;flex-direction:column;align-items:center;justify-content:center;text-align:center;padding:0 20px}
.feature h3{font-size:20px;font-weight:700;text-transform:uppercase;line-height:23px;margin-bottom:10px;max-width:460px}
.feature p{font-size:14px;line-height:21px;color:var(--muted);max-width:410px}
.btn-red{display:inline-block;margin-top:18px;background:var(--red);color:var(--white);font-size:14px;font-weight:700;padding:8px 11px;text-transform:uppercase}
.img-left .photo{left:0}.img-left .copy{left:700px}
.img-right .photo{left:500px}.img-right .copy{left:0}

/* clients */
.clients-title{left:0;top:4303px;width:1200px;text-align:center;font-size:21px;font-weight:700;text-transform:uppercase}
.clients-sub{left:0;top:4330px;width:1200px;text-align:center;font-size:14px;color:var(--muted)}
.clients{left:0;top:4357px;width:1200px;height:185px;display:flex;border-top:1px solid #e4e4e4}
.client{flex:1;border-right:1px solid #e4e4e4;display:flex;align-items:center;justify-content:center;color:#8a8a8a;font-size:30px}
.client:last-child{border-right:0}

/* footer */
.site-footer{left:0;top:4542px;width:1200px;height:481px;background:var(--footer);color:var(--white)}
.foot-col{top:36px;width:290px}
.foot-col h4{font-size:14px;font-weight:700;text-transform:uppercase;margin-bottom:10px}
.foot-col li{list-style:none;font-size:14px;line-height:21px}
.foot-links{left:0;top:390px;width:1200px;text-align:center;font-family:"Tinos",serif;font-size:13px;font-weight:700;word-spacing:2px}
.foot-links span{margin:0 10px}
.copyright{left:0;top:422px;width:1200px;text-align:center;font-size:13px}
.social{left:0;top:456px;width:1200px;display:flex;justify-content:center;gap:18px}
.social i{display:block;width:11px;height:11px;background:var(--white);border-radius:2px}
</style>
</head>
<body>

<header class="site-header abs">
  <div class="brand abs">Halvern Build</div>
  <div class="menu-btn abs">
    <svg width="14" height="12" viewBox="0 0 14 12"><rect y="0" width="14" height="2" fill="#fff"/><rect y="5" width="14" height="2" fill="#fff"/><rect y="10" width="14" height="2" fill="#fff"/></svg>
  </div>
</header>

<section class="hero abs" role="img" aria-label="Two construction workers in hard hats and orange safety vests on a sunny job site">
  <svg class="hero-arrow abs" style="left:20px" width="14" height="26" viewBox="0 0 14 26"><path d="M12 2 2 13l10 11" fill="none" stroke="#fff" stroke-width="2" opacity=".7"/></svg>
  <svg class="hero-arrow abs" style="right:20px" width="14" height="26" viewBox="0 0 14 26"><path d="m2 2 10 11L2 24" fill="none" stroke="#fff" stroke-width="2" opacity=".7"/></svg>
  <div class="hero-copy abs">
    <div class="hero-title">Proven delivery of<br>forward thinking<br>teaching environments</div>
    <div class="hero-sub">Marlow Ridge College, Sciences Building</div>
    <span class="btn-outline">Read More</span>
  </div>
</section>
<svg class="hero-scroll abs" width="24" height="24" viewBox="0 0 24 24" style="z-index:2"><circle cx="12" cy="12" r="12" fill="#e8141b"/><path d="M7 10l5 5 5-5" fill="none" stroke="#fff" stroke-width="2"/></svg>

<section class="intro abs">
  <h2>We have 10 years of experience in this field.<br>We know what you want.</h2>
  <p>We're a Modern Architect Studio Based in London UK. We are the top 3 earners of 2012, each making over $400 million US Dollars in Fee Income.it has developed a passionate audience of more than 25 million active monthly users and seemingly endless opportunities to shape the $300 billion designs.</p>
  <div class="video abs" role="img" aria-label="Video still of a steel-frame building under construction with a lift and workers">
    <div class="video-bar abs">
      <svg class="abs" style="left:28px;top:18px" width="12" height="14" viewBox="0 0 12 14"><rect width="4" height="14" fill="#fff"/><rect x="8" width="4" height="14" fill="#fff"/></svg>
      <svg class="abs" style="left:60px;top:22px" width="650" height="6"><rect width="650" height="4" y="1" fill="rgba(255,255,255,.35)"/><rect width="40" height="4" y="1" fill="#fff"/></svg>
      <svg class="abs" style="left:725px;top:18px" width="14" height="14" viewBox="0 0 14 14"><circle cx="7" cy="7" r="5" fill="none" stroke="#fff" stroke-width="3" stroke-dasharray="3 2"/></svg>
      <svg class="abs" style="left:750px;top:18px" width="14" height="14" viewBox="0 0 14 14"><path d="M1 5V1h4M9 1h4v4M13 9v4H9M5 13H1V9" fill="none" stroke="#fff" stroke-width="2"/></svg>
    </div>
  </div>
  <div class="btn-dark abs">More about Halvern Build</div>
</section>

<div class="service abs" style="left:21px">
  <svg width="50" height="50" viewBox="0 0 50 50" fill="none" stroke="#333" stroke-width="1.5"><path d="M25 8 4 18l21 10 21-10z"/><path d="m4 25 21 10 21-10"/><path d="m4 32 21 10 21-10"/></svg>
  <span>Interior Design</span>
</div>
<div class="service abs" style="left:418px">
  <svg width="50" height="50" viewBox="0 0 50 50" fill="none" stroke="#333" stroke-width="1.5"><circle cx="25" cy="12" r="4"/><path d="M25 4v4M22 15 13 42M28 15l9 27M15 34c6 4 14 4 20 0"/><path d="M8 30h34"/></svg>
  <span>Industrial Architecture</span>
</div>
<div class="service abs" style="left:814px">
  <svg width="50" height="50" viewBox="0 0 50 50" fill="none" stroke="#333" stroke-width="1.5"><rect x="5" y="5" width="40" height="40"/><path d="M18 32 38 12M26 12h12v12"/></svg>
  <span>Product Design</span>
</div>

<section class="stats abs">
  <div class="stat"><b>56</b><small>Awards Winning</small></div>
  <div class="stat"><b>954+</b><small>Project Completed</small></div>
  <div class="stat"><b>845+</b><small>Happy Customers</small></div>
  <div class="stat"><b>7165</b><small>Hours Worked</small></div>
</section>

<section class="feature img-left abs" style="top:1844px">
  <div class="photo" role="img" aria-label="Two workers in hard hats and orange vests walking on site" style="background:linear-gradient(160deg,#7fa6c6,#c27a3d 60%,#4b3d30)"></div>
  <div class="copy"><h3>A Corporate</h3><p>Lorem ipsum dolor sit amet, consectetur adipisicing elit, sed do eiusmodas temporo incididunt ut labore et dolore magna aliqua. Ut enim ad minim veniam, quis nostrd exercitation ullamco laboris nisi ut aliquip ex comodo consequat. Duis aute dolor in reprehenderit.</p><span class="btn-red">Learn More</span></div>
</section>

<section class="feature img-right abs" style="top:2311px">
  <div class="photo" role="img" aria-label="Smiling crew in safety vests resting together outdoors" style="background:linear-gradient(140deg,#5d6b3e,#b98a52 50%,#3e3a33)"></div>
  <div class="copy"><h3>Modern</h3><p>Lorem ipsum dolor sit amet, consectetur adipisicing elit, sed do eiusmodas temporo incididunt ut labore et dolore magna aliqua. Ut enim ad minim veniam, quis nostrd exercitation ullamco laboris nisi ut aliquip ex comodo consequat. Duis aute dolor in reprehenderit.</p><span class="btn-red">Learn More</span></div>
</section>

<section class="feature img-left abs" style="top:2777px">
  <div class="photo" role="img" aria-label="Worker pushing a wheelbarrow along a trench lined with cones" style="background:linear-gradient(170deg,#7c8a74,#a89a85 50%,#6e5e4c)"></div>
  <div class="copy"><h3>Reliable</h3><p>Lorem ipsum dolor sit amet, consectetur adipisicing elit, sed do eiusmodas temporo incididunt ut labore et dolore magna aliqua. Ut enim ad minim veniam, quis nostrd exercitation ullamco laboris nisi ut aliquip ex comodo consequat. Duis aute dolor in reprehenderit.</p><span class="btn-red">Learn More</span></div>
</section>

<section class="feature img-right abs" style="top:3243px">
  <div class="photo" role="img" aria-label="Gloved hands spraying water over a concrete saw" style="background:linear-gradient(150deg,#2e2a22,#6b4a2b 45%,#3a332b)"></div>
  <div class="copy"><h3>A friendly place to work with happy workers.</h3><p>Lorem ipsum dolor sit amet, consectetur adipisicing elit, sed do eiusmodas temporo incididunt ut labore et dolore magna aliqua. Ut enim ad minim veniam, quis nostrd exercitation ullamco laboris nisi ut aliquip ex comodo consequat. Duis aute dolor in reprehenderit.</p><span class="btn-red">Learn More</span></div>
</section>

<section class="feature img-left abs" style="top:3709px">
  <div class="photo" role="img" aria-label="Group of site managers in hard hats and vests talking" style="background:linear-gradient(160deg,#c9b89a,#b56a3a 50%,#3c3630)"></div>
  <div class="copy"><h3>Corvane Architecture &amp; Interior Pressline Theme</h3><p>We're a Modern Architect Studio Based in London UK. We are the top 3 earners of 2012, each making over $400 million US Dollars in Fee Income.it has developed a passionate audience of more than 25 million active monthly users.</p><span class="btn-red">Learn More</span></div>
</section>

<div class="clients-title abs">Trusted Clients</div>
<div class="clients-sub abs">We have worked with some of great clients in worldwide.</div>
<div class="clients abs">
  <div class="client">Quillon</div>
  <div class="client">Quillon</div>
  <div class="client">Quillon</div>
  <div class="client">Quillon</div>
</div>

<footer class="site-footer abs">
  <div class="foot-col abs" style="left:8px"><h4>About Us</h4><ul><li>About Halvern Build</li><li>People</li><li>Giving Back</li><li>Affiliates</li><li>Safety</li><li>Rankings</li><li>Awards</li><li>Civic Builders Guild</li></ul></div>
  <div class="foot-col abs" style="left:308px"><h4>Expertise</h4><ul><li>In Progress</li><li>Biomedical/Life Sciences</li><li>Civic &amp; Cultural</li><li>Commercial &amp; Office</li><li>Community College Districts</li><li>Education – K-12</li><li>Entertainment &amp; Sports</li><li>Healthcare</li><li>Higher Education</li><li>Hospitality &amp; Gaming</li><li>Parking</li><li>Residential</li><li>Retail</li><li>Senior Living</li><li>Sustainable</li></ul></div>
  <div class="foot-col abs" style="left:609px"><h4>Services</h4><ul><li>Preconstruction</li><li>Construction</li><li>Close-Out</li><li>BIM</li><li>Delivery Methods</li></ul></div>
  <div class="foot-col abs" style="left:909px"><h4>Careers</h4><ul><li>Overview</li><li>Openings</li><li>College Recruiting &amp; Internships</li><li>Recruiting Events</li><li>Our Benefits</li><li>Professional Development</li></ul></div>
  <div class="foot-links abs"><span>NEWS</span><span>CONTACT US</span><span>BUILD WITH US</span></div>
  <div class="copyright abs">Copyright © 2019</div>
  <div class="social abs"><i></i><i></i><i></i><i></i><i></i></div>
</footer>

</body>
</html>
```